Business Card Design for Vantor Gear

We want to have a business card design for our company.
Company website: www.vantorgear-example.com.au
We looking for something cool, funky, and impressive, yet elegant.
Below are the contents that should be displayed on the card:
Front:
Name: Mark Dellow
Title: Sales & Purchasing
Company Name: Vantor Gear Pty Ltd
Phone: 02 5550 1473
Mobile: 0400 555 019
Email: mark@vantorgear-example.com.au
Website: www.vantorgear-example.com.au
Address: 17 Brackley St
Carrowmere, NSW 2990
Back:
We buy sell new used Norvex and network equipment
• Huge Savings - save up to 95% off list prices
• Highest Reliability
• Comprehensive Warranty
• Fast delivery
• Large range of hardware in stock
Our logo can be downloaded at: www.vantorgear-example.com.au/logo.zip

```html
<!DOCTYPE html>
<html lang="en">
<head>
<meta charset="utf-8">
<title>Vantor Gear – Business Card</title>
<link href="https://fonts.googleapis.com/css2?family=Arimo:wght@400;700&display=swap" rel="stylesheet">
<style>
  :root {
    --blue: #1f2ee0;
    --blue-deep: #1420c8;
    --cyan: #20d6f2;
    --white: #ffffff;
    --orange: #f39a16;
    --ink: #3a3a3a;
    --name-blue: #1a8fd8;
    --backdrop: #eef0f2;
  }
  * { margin: 0; padding: 0; box-sizing: border-box; }
  html, body { width: 1200px; height: 900px; overflow: hidden; }
  body {
    background: var(--backdrop);
    font-family: "Arimo", Arial, sans-serif;
    display: flex;
    flex-direction: column;
    align-items: center;
    justify-content: center;
    gap: 34px;
  }
  .card {
    position: relative;
    width: 700px;
    height: 400px;
    background: var(--white);
    overflow: hidden;
    box-shadow: 0 4px 14px rgba(0,0,0,0.18);
  }
  .card-shapes { position: absolute; inset: 0; width: 100%; height: 100%; }

  /* Front */
  .brand {
    position: absolute;
    left: 34px;
    top: 30px;
    display: flex;
    align-items: center;
    gap: 16px;
  }
  .brand-dot {
    width: 84px; height: 84px;
    border-radius: 50%;
    background: var(--orange);
  }
  .brand-text { display: flex; flex-direction: column; }
  .brand-name {
    color: var(--white);
    font-weight: 700;
    font-size: 54px;
    line-height: 1;
    letter-spacing: -0.5px;
  }
  .brand-tagline {
    color: var(--white);
    font-size: 11px;
    letter-spacing: 4px;
    margin-top: 6px;
    margin-left: 4px;
  }
  .person {
    position: absolute;
    left: 40px;
    top: 200px;
    width: 210px;
    text-align: right;
  }
  .person-name {
    color: var(--name-blue);
    font-weight: 700;
    font-size: 20px;
    text-transform: uppercase;
    letter-spacing: 0.5px;
  }
  .person-title {
    color: var(--orange);
    font-weight: 700;
    font-size: 17px;
    margin-top: 4px;
  }
  .divider {
    position: absolute;
    left: 266px;
    top: 192px;
    height: 98px;
    border-left: 2px dotted var(--name-blue);
  }
  .contacts {
    position: absolute;
    left: 280px;
    top: 194px;
    list-style: none;
    color: var(--ink);
    font-size: 16px;
    font-weight: 700;
  }
  .contacts li { display: flex; align-items: center; gap: 8px; height: 30px; }
  .contacts svg { width: 16px; height: 16px; flex: none; }
  .contacts .pair { margin-left: 14px; display: flex; align-items: center; gap: 8px; }
  .address {
    position: absolute;
    right: 34px;
    bottom: 20px;
    color: var(--white);
    font-weight: 700;
    font-size: 19px;
  }

  /* Back */
  .headline {
    position: absolute;
    left: 28px;
    top: 48px;
    color: var(--white);
    font-weight: 700;
    font-size: 20px;
    text-transform: uppercase;
  }
  .benefits {
    position: absolute;
    left: 52px;
    top: 176px;
    list-style: none;
    color: var(--ink);
    font-size: 19px;
    font-weight: 700;
    letter-spacing: 0.3px;
  }
  .benefits li { position: relative; height: 26px; }
  .benefits li::before {
    content: "";
    position: absolute;
    left: -16px; top: 8px;
    width: 7px; height: 7px;
    border-radius: 50%;
    background: var(--orange);
  }
</style>
</head>
<body>

<section class="card card-front" aria-label="Business card front">
  <svg class="card-shapes" viewBox="0 0 700 400" preserveAspectRatio="none" aria-hidden="true">
    <defs>
      <linearGradient id="front-top" x1="0" y1="0" x2="1" y2="0">
        <stop offset="0" stop-color="#2fd2f4"/>
        <stop offset="0.35" stop-color="#2466ea"/>
        <stop offset="1" stop-color="#1f2ee0"/>
      </linearGradient>
      <linearGradient id="front-bottom" x1="0" y1="0" x2="1" y2="0">
        <stop offset="0" stop-color="#21e0f4"/>
        <stop offset="0.45" stop-color="#1f8ef0"/>
        <stop offset="0.62" stop-color="#1f2ee0"/>
        <stop offset="1" stop-color="#1f2ee0"/>
      </linearGradient>
    </defs>
    <path d="M0 0 H700 V118 H540 C500 118 495 150 455 150 H0 Z" fill="url(#front-top)"/>
    <path d="M110 400 V352 C110 336 120 330 140 330 H700 V400 Z" fill="url(#front-bottom)"/>
  </svg>

  <div class="brand">
    <span class="brand-dot"></span>
    <div class="brand-text">
      <span class="brand-name">Vantor Gear</span>
      <span class="brand-tagline">NETWORKING EQUIPMENT</span>
    </div>
  </div>

  <div class="person">
    <p class="person-name">Mark Dellow</p>
    <p class="person-title">Sales &amp; Purchasing</p>
  </div>
  <div class="divider"></div>

  <ul class="contacts">
    <li>
      <svg viewBox="0 0 16 16"><path d="M4 1 L6.5 4 L5 6 C6 8.5 7.5 10 10 11 L12 9.5 L15 12 L13 15 C7 14.5 1.5 9 1 3 Z" fill="#f39a16"/></svg>
      02 5550 1473
      <span class="pair">
        <svg viewBox="0 0 16 16"><rect x="4" y="1" width="8" height="14" rx="1.5" fill="#f39a16"/><rect x="5.5" y="3" width="5" height="7" fill="#fff"/></svg>
        0400 555 019
      </span>
    </li>
    <li>
      <svg viewBox="0 0 16 16"><rect x="1" y="3" width="14" height="10" fill="#f39a16"/><path d="M1 3 L8 9 L15 3" fill="none" stroke="#fff" stroke-width="1.4"/></svg>
      mark@vantorgear-example.com.au
    </li>
    <li>
      <svg viewBox="0 0 16 16"><circle cx="8" cy="8" r="7" fill="#f39a16"/><path d="M1 8 H15 M8 1 C4 5 4 11 8 15 M8 1 C12 5 12 11 8 15" fill="none" stroke="#fff" stroke-width="1"/></svg>
      www.vantorgear-example.com.au
    </li>
  </ul>

  <p class="address">17 Brackley St Carrowmere, NSW 2990</p>
</section>

<section class="card card-back" aria-label="Business card back">
  <svg class="card-shapes" viewBox="0 0 700 400" preserveAspectRatio="none" aria-hidden="true">
    <defs>
      <linearGradient id="back-top" x1="0" y1="0" x2="1" y2="0">
        <stop offset="0" stop-color="#1f2ee0"/>
        <stop offset="0.6" stop-color="#1f3ee4"/>
        <stop offset="1" stop-color="#22d8f2"/>
      </linearGradient>
      <linearGradient id="back-bottom" x1="0" y1="0" x2="1" y2="0">
        <stop offset="0" stop-color="#1f2ee0"/>
        <stop offset="0.55" stop-color="#1f3ee4"/>
        <stop offset="1" stop-color="#22d8f2"/>
      </linearGradient>
    </defs>
    <path d="M0 0 H700 V140 H620 C580 140 575 160 540 160 H0 Z" fill="url(#back-top)"/>
    <path d="M0 400 V338 H520 C560 338 565 310 610 310 H700 V400 Z" fill="url(#back-bottom)"/>
  </svg>

  <h2 class="headline">We buy sell new used Norvex &amp; network equipment</h2>

  <ul class="benefits">
    <li>Huge Savings - save up to 95% off list prices</li>
    <li>Highest Reliability</li>
    <li>Comprehensive Warranty</li>
    <li>Fast delivery</li>
    <li>Large range of hardware in stock</li>
  </ul>
</section>

</body>
</html>
```